Business Cards

Need a neat design for a new business card

Industry/Entity Type

Residential Construction

Contact Information for Business Card

Company Name- KOVE Construction Inc.
Owner- Marcus Tolliver
Phone number- (555)203-7481
Email- kovecohomes@brindlemail.example
Facebook- www.socialpage.example/kovecohomes

Colors
fefdec

```html
<!DOCTYPE html>
<html lang="en">
<head>
<meta charset="utf-8">
<title>KOVE Construction Inc. – Business Card</title>
<link rel="stylesheet" href="https://fonts.googleapis.com/css2?family=Arimo:wght@400;700&display=swap">
<style>
  :root {
    --page-bg: #e8e5e2;
    --card-bg: #000000;
    --card-text: #ffffff;
    --badge-light: #fbfafa;
    --badge-mid: #e6e2e2;
    --badge-edge: #d2cccc;
    --badge-text: #111111;
  }
  html, body {
    margin: 0;
    width: 1200px;
    height: 900px;
    overflow: hidden;
    background: var(--page-bg);
    font-family: "Arimo", Arial, sans-serif;
  }
  .business-card {
    position: absolute;
    left: 100px;
    top: 140px;
    width: 1000px;
    height: 620px;
    background: var(--card-bg);
    color: var(--card-text);
    box-shadow: 0 18px 40px rgba(0,0,0,0.25);
  }
  .owner-name {
    position: absolute;
    left: 60px;
    top: 78px;
    margin: 0;
    font-size: 37px;
    font-weight: 700;
    letter-spacing: 0.3px;
    line-height: 1;
  }
  .owner-role {
    position: absolute;
    left: 59px;
    top: 124px;
    margin: 0;
    font-size: 27px;
    font-weight: 400;
    line-height: 1;
  }
  .contact-list {
    position: absolute;
    left: 58px;
    top: 420px;
    margin: 0;
    padding: 0;
    list-style: none;
  }
  .contact-item {
    display: flex;
    align-items: center;
    height: 37px;
    font-size: 28px;
    line-height: 1;
  }
  .contact-icon {
    width: 28px;
    height: 28px;
    margin-right: 11px;
    flex: none;
  }
  .brand-badge {
    position: absolute;
    left: 500px;
    top: 82px;
    width: 450px;
    height: 450px;
    border-radius: 50%;
    background: radial-gradient(circle at 45% 40%, var(--badge-light) 0%, var(--badge-mid) 65%, var(--badge-edge) 100%);
    display: flex;
    flex-direction: column;
    align-items: center;
    justify-content: center;
    color: var(--badge-text);
    font-weight: 400;
  }
  .brand-name {
    font-size: 92px;
    line-height: 1;
    letter-spacing: 4px;
    margin-top: 40px;
  }
  .brand-sub {
    font-size: 25px;
    letter-spacing: 4px;
    margin-top: 22px;
  }
</style>
</head>
<body>
  <article class="business-card">
    <h1 class="owner-name">MARCUS TOLLIVER</h1>
    <p class="owner-role">Owner</p>

    <ul class="contact-list">
      <li class="contact-item">
        <svg class="contact-icon" viewBox="0 0 24 24" aria-hidden="true">
          <path d="M6.6 3.5l3 3.2-1.8 2.2c1.2 2.6 3.2 4.6 5.8 5.8l2.2-1.8 3.2 3-1.9 3c-7.4-.4-13.3-6.3-13.7-13.7z" fill="none" stroke="#fff" stroke-width="1.8" stroke-linejoin="round"/>
          <path d="M14 3.5a6.5 6.5 0 0 1 6.5 6.5M14 7a3 3 0 0 1 3 3" fill="none" stroke="#fff" stroke-width="1.8" stroke-linecap="round"/>
        </svg>
        (555)203-7481
      </li>
      <li class="contact-item">
        <svg class="contact-icon" viewBox="0 0 24 24" aria-hidden="true">
          <rect x="2" y="5" width="20" height="14" fill="#fff"/>
          <path d="M2 5l10 8 10-8M2 19l7.5-7M22 19l-7.5-7" fill="none" stroke="#000" stroke-width="1.4"/>
        </svg>
        kovecohomes@brindlemail.example
      </li>
      <li class="contact-item">
        <svg class="contact-icon" viewBox="0 0 24 24" aria-hidden="true">
          <circle cx="12" cy="12" r="6" fill="#fff"/>
        </svg>
        www.socialpage.example/kovecohomes
      </li>
    </ul>

    <div class="brand-badge">
      <span class="brand-name">KOVE</span>
      <span class="brand-sub">CONSTRUCTION</span>
    </div>
  </article>
</body>
</html>
```